Business Card Design

5* Hotel Property based on an island in Greece

My position is aparta from being a director, i'm on the accounts payable too, not sure how this should be stated, with a comma or "/"?

Sorry about the uploaded logo, it was a mistaken one!

There's also need to be added this  www.corvanteholdings.com on the back side of the card!

Also need to have the logo of the corvante holdings which can be found in a second on the brief! Thank you guys, irini

Industry/Entity Type

Business

Contact Information for Business Card

VERISTOKA PELLA Hotel
Irini Dravetsou
Director, AP Dept.

www.veristoka.gr
Peltira Island 85300
Greece

irinidravetsou@fenmail.com
+306951273064

```html
<!DOCTYPE html>
<html lang="en">
<head>
<meta charset="utf-8">
<title>Veristoka Pella Hotel – Business Card</title>
<link rel="stylesheet" href="https://fonts.googleapis.com/css2?family=Open+Sans:ital,wght@0,400;1,400&family=EB+Garamond:wght@400&display=swap">
<style>
  :root {
    --page-bg: #e8e9eb;
    --navy-deep: #0c1a45;
    --navy-mid: #17336f;
    --sea-blue: #2e6fbe;
    --ink-white: #ffffff;
    --ink-soft: #dfe6f3;
    --gold: #e2a92b;
    --mark-blue: #3f8fd8;
  }
  * { box-sizing: border-box; margin: 0; padding: 0; }
  html, body {
    width: 1000px; height: 1200px; overflow: hidden;
    background: var(--page-bg);
  }
  .sheet { position: relative; width: 1000px; height: 1200px; }

  .card {
    position: absolute; left: 70px; width: 860px; height: 520px;
    overflow: hidden;
    background: linear-gradient(160deg, var(--navy-deep) 0%, var(--navy-mid) 45%, var(--sea-blue) 100%);
    box-shadow: 0 6px 18px rgba(0,0,0,0.18);
  }
  .card--front { top: 50px; }
  .card--back { top: 630px; }

  .brand {
    position: absolute; display: flex; align-items: center;
    color: var(--ink-white);
    font-family: "Open Sans", sans-serif; font-weight: 400;
    line-height: 1.02; letter-spacing: 0.5px;
  }
  .brand__square {
    flex: none; background: var(--mark-blue);
    border: 3px solid var(--ink-white);
  }
  .card--front .brand { left: 18px; top: 16px; font-size: 25px; }
  .card--front .brand__square { width: 60px; height: 60px; margin-right: 10px; }
  .card--back .brand { left: 60px; top: 38px; font-size: 38px; }
  .card--back .brand__square { width: 100px; height: 100px; margin-right: 16px; }

  .website {
    position: absolute; left: 176px; top: 148px;
    font-family: "EB Garamond", serif; font-size: 30px;
    color: var(--ink-white);
  }

  .decor { position: absolute; border-radius: 50%; }
  .decor--bubbles {
    left: 250px; top: -70px; width: 640px; height: 420px;
    background:
      radial-gradient(ellipse at 88% 18%, rgba(226,169,43,0.55) 0%, rgba(226,169,43,0) 18%),
      radial-gradient(ellipse at 62% 40%, rgba(200,225,255,0.55) 0%, rgba(90,150,230,0.4) 28%, rgba(50,110,200,0.15) 55%, rgba(40,90,180,0) 75%);
  }
  .decor--swirl-top {
    left: 560px; top: -60px; width: 360px; height: 260px;
    background: radial-gradient(ellipse at 60% 50%, rgba(150,170,230,0.3) 0%, rgba(110,130,210,0) 70%);
  }
  .decor--swirl-bottom {
    left: -90px; top: 290px; width: 440px; height: 320px;
    background: radial-gradient(ellipse at 40% 60%, rgba(170,210,255,0.45) 0%, rgba(90,150,230,0.18) 45%, rgba(60,120,210,0) 72%);
  }

  .group {
    position: absolute; right: 36px; bottom: 30px; text-align: right;
    color: var(--ink-white);
  }
  .group__brand {
    display: flex; align-items: center; justify-content: flex-end;
    font-family: "Open Sans", sans-serif; font-size: 17px; letter-spacing: 1.5px;
  }
  .group__square {
    width: 16px; height: 16px; margin-right: 8px;
    border: 2px solid var(--ink-white);
  }
  .group__web {
    margin-top: 4px;
    font-family: "EB Garamond", serif; font-size: 20px; color: var(--ink-soft);
  }

  .person {
    position: absolute; right: 94px; top: 256px; text-align: right;
    color: var(--ink-white);
  }
  .person__name {
    font-family: "EB Garamond", serif; font-size: 48px; line-height: 1;
  }
  .person__role {
    margin-top: 8px;
    font-family: "Open Sans", sans-serif; font-style: italic; font-size: 18px;
    color: var(--ink-soft);
  }

  .contacts {
    position: absolute; left: 392px; top: 376px; list-style: none;
  }
  .contacts__item {
    display: flex; align-items: center; height: 42px;
    font-family: "EB Garamond", serif; font-size: 24px; color: var(--ink-soft);
  }
  .contacts__icon { width: 22px; height: 22px; margin-right: 30px; flex: none; }
</style>
</head>
<body>
<main class="sheet">

  <section class="card card--front" aria-label="Card front">
    <div class="decor decor--bubbles" role="img" aria-label="Decorative cluster of bubbles, gold dots and outlined squares"></div>
    <div class="brand">
      <span class="brand__square"></span>
      <span class="brand__name">VERISTOKA<br>PELLA HOTEL</span>
    </div>
    <div class="group">
      <p class="group__brand"><span class="group__square"></span>CORVANTE HOLDINGS</p>
      <p class="group__web">www.corvanteholdings.com</p>
    </div>
  </section>

  <section class="card card--back" aria-label="Card back">
    <div class="decor decor--swirl-top" role="img" aria-label="Decorative floral swirl ornament"></div>
    <div class="decor decor--swirl-bottom" role="img" aria-label="Decorative wave swirl ornament with bubbles"></div>

    <div class="brand">
      <span class="brand__square"></span>
      <span class="brand__name">VERISTOKA<br>PELLA HOTEL</span>
    </div>
    <p class="website">www.veristoka.gr</p>

    <div class="person">
      <p class="person__name">Irini Dravetsou</p>
      <p class="person__role">Director , AP Dept.</p>
    </div>

    <ul class="contacts">
      <li class="contacts__item">
        <svg class="contacts__icon" viewBox="0 0 24 24" aria-hidden="true">
          <path fill="var(--gold)" d="M12 2a7 7 0 0 0-7 7c0 5 7 13 7 13s7-8 7-13a7 7 0 0 0-7-7zm0 9.5A2.5 2.5 0 1 1 12 6.5a2.5 2.5 0 0 1 0 5z"/>
        </svg>
        Peltira Island,85300,Greece
      </li>
      <li class="contacts__item">
        <svg class="contacts__icon" viewBox="0 0 24 24" aria-hidden="true">
          <rect x="2" y="5" width="20" height="14" rx="1.5" fill="var(--gold)"/>
          <path d="M3 6l9 7 9-7" fill="none" stroke="var(--navy-mid)" stroke-width="1.6"/>
        </svg>
        irinidravetsou@fenmail.com
      </li>
      <li class="contacts__item">
        <svg class="contacts__icon" viewBox="0 0 24 24" aria-hidden="true">
          <path fill="var(--gold)" d="M6.6 10.8a15 15 0 0 0 6.6 6.6l2.2-2.2a1 1 0 0 1 1-.25 11.4 11.4 0 0 0 3.6.57 1 1 0 0 1 1 1V20a1 1 0 0 1-1 1A17 17 0 0 1 3 4a1 1 0 0 1 1-1h3.5a1 1 0 0 1 1 1c0 1.25.2 2.45.57 3.6a1 1 0 0 1-.25 1z"/>
        </svg>
        +306951273064
      </li>
    </ul>
  </section>

</main>
</body>
</html>
```